Branding flyers and marketing brochure templates

We are after corporate design templates for the following: 1. Flyer to advertise a course - include course name, course unit code, summary of course, entry requirements, price, course description. 2. Price list - to use for each office location, listing all courses - include course name, course unit code, date/time, price - also include section/key to notify for each course if funding is available 3. Marketing flyer template - to advertise government funding options that we have which a student may be eligible for (see 'funding' tab on our webpage ridgewardlearning.edu.au - we need one for each Diploma 2 Pledge and Learner Path. We want each of these templates to have similar designs and branding. There will be future work involved for creating more templates of similar branding for the correct person.

Files must be editable, preferably given as word, publisher or editable pdf.

Colors
9bcb3c

Requirements
Must have
• Green

```html
<!DOCTYPE html>
<html lang="en">
<head>
<meta charset="utf-8">
<title>Work Safely at Heights – Course Flyer</title>
<link href="https://fonts.googleapis.com/css2?family=Open+Sans:ital,wght@0,400;0,600;0,700;0,800;1,700;1,800&display=swap" rel="stylesheet">
<style>
  :root {
    --page-bg: #c9cacc;
    --paper: #ffffff;
    --green: #9bcb3c;
    --green-deep: #5fb51e;
    --red: #c0171a;
    --red-deep: #a50f12;
    --ink: #1d1d1d;
    --sky: #9fb7cc;
    --sky-deep: #4f6272;
  }
  * { box-sizing: border-box; margin: 0; padding: 0; }
  html, body { width: 1200px; height: 795px; overflow: hidden; }
  body {
    background: var(--page-bg);
    font-family: "Open Sans", sans-serif;
    display: flex; align-items: center; justify-content: center;
  }
  .flyer {
    position: relative;
    width: 540px; height: 764px;
    background: var(--paper);
    overflow: hidden;
    box-shadow: 0 4px 14px rgba(0,0,0,.18);
  }
  .flyer-art { position: absolute; inset: 0; }
  .brand {
    position: absolute; top: 48px; left: 0; width: 100%;
    text-align: center;
    display: flex; align-items: center; justify-content: center; gap: 10px;
  }
  .brand-mark { width: 16px; height: 16px; border-radius: 50%; background: var(--red); }
  .brand-name {
    font-weight: 700; font-size: 17px; letter-spacing: .08em;
    text-transform: uppercase; color: var(--ink);
  }
  .content {
    position: absolute; top: 186px; left: 30px; width: 490px;
    color: var(--ink);
  }
  .photo-wrap {
    float: right; width: 300px; height: 236px;
    shape-outside: polygon(42px 0, 300px 0, 300px 236px, 252px 236px);
  }
  .section-title {
    color: var(--red);
    font-weight: 800; font-style: italic;
    font-size: 17px; text-transform: uppercase;
    letter-spacing: .02em; margin-bottom: 3px;
  }
  .body-text {
    font-weight: 600; font-size: 12px; line-height: 1.45;
    margin-bottom: 14px;
  }
  .elements { list-style: none; font-weight: 600; font-size: 12.5px; line-height: 1.5; }
  .footer {
    position: absolute; left: 0; bottom: 0; width: 100%; height: 78px;
    background: linear-gradient(180deg, var(--red), var(--red-deep));
    display: flex; align-items: center; justify-content: space-between;
    padding: 0 26px; color: #fff; font-weight: 700;
  }
  .contact { display: flex; align-items: center; gap: 9px; font-size: 17px; }
  .contact svg { width: 22px; height: 22px; }
</style>
</head>
<body>
  <article class="flyer">
    <svg class="flyer-art" viewBox="0 0 540 764" aria-hidden="true">
      <defs>
        <linearGradient id="headerGreen" x1="0" y1="0" x2="1" y2="1">
          <stop offset="0" stop-color="#7ed321"/>
          <stop offset="1" stop-color="#4fae16"/>
        </linearGradient>
        <linearGradient id="photoTone" x1="0" y1="0" x2="1" y2="1">
          <stop offset="0" stop-color="#dfe8ee"/>
          <stop offset=".45" stop-color="#9fb7cc"/>
          <stop offset=".75" stop-color="#e1662a"/>
          <stop offset="1" stop-color="#4f6272"/>
        </linearGradient>
      </defs>
      <polygon class="header-band" points="0,0 540,0 540,146 0,168" fill="url(#headerGreen)"/>
      <polygon class="photo-accent" points="222,150 540,150 540,440 478,440" fill="var(--green-deep)"/>
      <polygon class="course-photo" role="img" aria-label="Photo of two site workers in hard hats and hi-vis vests on a high-rise construction site"
               points="240,150 540,150 540,422 470,422" fill="url(#photoTone)"/>
    </svg>

    <div class="brand">
      <span class="brand-mark"></span>
      <span class="brand-name">Ridgeward Training</span>
    </div>

    <div class="content">
      <div class="photo-wrap"></div>
      <h2 class="section-title">Work Safely at Heights :</h2>
      <p class="body-text">This nationally accredited Working at Heights course will equip you with the skills and knowledge that you require to safely work at heights. Our engaging course uses various forms of depth utilising fall protection. On the successful completion of the course, learners will be issued a nationally accredited ‘statement of attainment’ – RIIWHS204D – Work Safely at Heights.</p>

      <h2 class="section-title">Course Duration &amp; Overview :</h2>
      <p class="body-text">The course lasts approximately 1 day (approximately 8 hours) depending on the number of attendees and their prior knowledge and experience in the industry. There are no formal entry requirements for this course. You may be required to complete a Language, Literacy and Numeracy (LLN) indicator prior to enrolling.</p>

      <h2 class="section-title">The Elements of this Course Are :</h2>
      <ol class="elements">
        <li>1. Identify work requirements</li>
        <li>2. Identify work procedures and instructions</li>
        <li>3. Access and install equipment</li>
        <li>4. Perform work at heights</li>
        <li>5. Clean up work area</li>
      </ol>
    </div>

    <footer class="footer">
      <div class="contact">
        <svg viewBox="0 0 24 24" aria-hidden="true"><circle cx="12" cy="12" r="10.5" fill="none" stroke="#fff" stroke-width="2"/><path d="M8.5 7c-.8.6-1 1.8-.4 3.2 1 2.3 2.9 4.2 5.2 5.2 1.4.6 2.6.4 3.2-.4l-1.8-1.8-1.4.8c-1.2-.6-2.1-1.5-2.8-2.8l.8-1.4z" fill="#fff"/></svg>
        <span>+61 400 555 218</span>
      </div>
      <div class="contact">
        <svg viewBox="0 0 24 24" aria-hidden="true" fill="none" stroke="#fff" stroke-width="1.8"><circle cx="12" cy="12" r="10"/><ellipse cx="12" cy="12" rx="4.5" ry="10"/><path d="M2 12h20M4 7h16M4 17h16"/></svg>
        <span>www.ridgewardlearning.edu.au</span>
      </div>
    </footer>
  </article>
</body>
</html>
```